Website for Excavator and Earthworks Company

We require a modern, sleek and practical website for our newly created earthworks/excavator business in Perth, Western Australia called Gullwind Stonecut Earthworks.

The website should have a modern, cutting edge feel but only needs to be relatively simplistic in it's layout and eventual functionality.

Some pages it should have would be Home, About, Projects and Contact Us.

Number of Pages Required

1 page

```html
<!DOCTYPE html>
<html lang="en">
<head>
<meta charset="utf-8">
<title>Gullwind Stonecut Earthworks</title>
<link href="https://fonts.googleapis.com/css2?family=Archivo+Black&family=Montserrat:wght@400;500;600;700&display=swap" rel="stylesheet">
<style>
:root{
  --olive:#333a05;
  --olive-dark:#222503;
  --charcoal:#2b2a22;
  --black:#0d0d0b;
  --cta-black:#141412;
  --lime:#c9dc00;
  --white:#ffffff;
  --muted:#b8b8a8;
  --photo-sky:#8a8f86;
  --photo-yellow:#d99a14;
  --photo-rock:#5d5f58;
  --star:#f4c21b;
  --badge-blue:#2e6bb0;
}
*{box-sizing:border-box;margin:0;padding:0}
html,body{width:1200px;height:3858px;overflow:hidden}
body{position:relative;background:var(--olive);font-family:"Montserrat",sans-serif;color:var(--white)}
.abs{position:absolute}
.display{font-family:"Archivo Black",sans-serif;line-height:1.05}
.btn{position:absolute;display:flex;align-items:center;justify-content:center;font-weight:700;font-size:15px;text-transform:uppercase;border-radius:4px}
.btn-lime{background:var(--lime);color:#1a1a0a}
.btn-ghost{border:2px solid var(--white);color:var(--white)}
.photo{position:absolute;background:linear-gradient(160deg,var(--photo-sky) 0%,var(--photo-yellow) 45%,var(--photo-rock) 100%)}

/* header */
.topbar{left:735px;top:0;width:465px;height:36px;background:var(--olive-dark);clip-path:polygon(0 0,100% 0,100% 100%,6% 100%);display:flex;align-items:center;justify-content:flex-end;gap:30px;padding-right:50px;font-size:12px;font-weight:600}
.topbar span{display:flex;align-items:center;gap:8px}
.brand{display:flex;align-items:center;gap:10px}
.brand-mark{width:22px;height:22px;background:var(--lime)}
.brand-name{font-weight:700;font-size:17px;line-height:1.1;text-transform:uppercase;color:var(--white)}
.nav{left:527px;top:74px;font-size:13px;font-weight:700}
.nav a{position:absolute;white-space:nowrap}

/* hero */
.trusted{left:50px;top:140px;width:355px;height:34px;background:var(--black);border-radius:4px;display:flex;align-items:center;gap:8px;padding-left:24px;font-size:13px;font-weight:700;text-transform:uppercase}
.stars{display:flex;gap:3px}
.hero-title{left:50px;top:190px;font-size:58px;text-transform:uppercase;line-height:66px;white-space:nowrap;z-index:2}
.hero-text{left:50px;top:480px;width:400px;font-size:15px;line-height:1.45}

/* about */
.stat{position:absolute;width:262px;height:116px;background:var(--olive-dark);border-radius:4px;padding:28px 26px}
.stat-label{font-size:13px;font-weight:600;letter-spacing:1.5px;text-transform:uppercase}
.stat-value{font-family:"Archivo Black",sans-serif;font-size:30px;color:var(--lime);margin-top:14px}
.about-title{left:608px;top:1036px;font-size:58px;line-height:66px;white-space:nowrap}
.about-text{left:608px;top:1253px;width:530px;font-size:13.5px;line-height:1.5}

/* services */
.section-title{font-size:60px}
.service-card{position:absolute;top:1665px;width:333px;height:432px;background:var(--olive-dark);clip-path:polygon(0 5%,52% 0,100% 8%,100% 95%,0 100%);padding:75px 35px 0}
.service-card h3{font-size:20px;font-weight:700;letter-spacing:1px;text-transform:uppercase;line-height:1.35}
.service-card p{margin-top:26px;font-size:13px;line-height:1.55;color:var(--muted);width:210px}
.see-more{position:absolute;left:39px;bottom:65px;display:flex;align-items:center;gap:10px;font-size:13px;font-weight:700;color:var(--lime);text-transform:uppercase}

/* why */
.why-card{position:absolute;top:2337px;width:156px;height:183px;background:var(--olive-dark);border-radius:6px;padding:30px 23px}
.why-icon{width:53px;height:53px;background:var(--lime);border-radius:3px;display:flex;align-items:center;justify-content:center}
.why-card p{margin-top:20px;font-size:13px;font-weight:600;text-transform:uppercase;line-height:1.5}

/* testimonial */
.quote-card{left:259px;top:2690px;width:681px;height:218px;background:var(--olive-dark);border-radius:8px;padding:42px 58px}
.arrow-circle{position:absolute;width:30px;height:30px;border-radius:50%;background:var(--black);border:1px solid var(--white);display:flex;align-items:center;justify-content:center}
.dot{position:absolute;top:2937px;width:7px;height:7px;border-radius:50%;background:var(--white)}

/* cta */
.cta{left:50px;top:3057px;width:1100px;height:323px;background:var(--cta-black);border-radius:8px}

/* footer */
.footer{left:0;top:3455px;width:1200px;height:403px;background:var(--black)}
.footer-heading{position:absolute;font-size:21px;font-weight:700}
.footer-links a{position:absolute;font-size:15px;color:#e6e6e6}
.contact-row{position:absolute;left:886px;display:flex;align-items:center;gap:16px;font-size:13px}
.contact-dot{width:32px;height:32px;border-radius:50%;background:var(--lime);display:flex;align-items:center;justify-content:center}
.social{position:absolute;top:3738px;width:25px;height:25px;border-radius:50%;background:var(--white)}
</style>
</head>
<body>

<!-- Header -->
<div class="abs topbar">
  <span><svg width="16" height="16" viewBox="0 0 24 24" fill="none" stroke="#fff" stroke-width="2"><path d="M5 3h4l2 5-3 2a12 12 0 0 0 6 6l2-3 5 2v4a2 2 0 0 1-2 2A17 17 0 0 1 3 5a2 2 0 0 1 2-2z"/></svg>+1 555-014-8720</span>
  <span><svg width="16" height="16" viewBox="0 0 24 24" fill="none" stroke="#fff" stroke-width="2"><rect x="3" y="5" width="18" height="14" rx="2"/><path d="M3 7l9 6 9-6"/></svg>hello@gullwindstonecut.example</span>
</div>
<div class="abs brand" style="left:50px;top:62px">
  <div class="brand-mark"></div>
  <div class="brand-name">Gullwind Stonecut<br>Earthworks</div>
</div>
<nav class="abs nav">
  <a style="left:0;top:0">SERVICE</a>
  <a style="left:111px;top:0">PROJECTS</a>
  <a style="left:236px;top:0">PROCESS</a>
  <a style="left:353px;top:0">SAFETY</a>
</nav>
<div class="btn btn-lime" style="left:986px;top:58px;width:164px;height:48px">Request Quote</div>

<!-- Hero -->
<div class="photo" role="img" aria-label="Yellow tracked excavator on gravel in a mountain valley" style="left:435px;top:132px;width:765px;height:511px;clip-path:polygon(24% 0,100% 0,100% 100%,0 100%)"></div>
<div class="abs trusted">Trusted by thousands
  <span class="stars">
    <svg width="15" height="15" viewBox="0 0 24 24"><path fill="var(--star)" d="M12 2l3 7 7 .6-5.4 4.7 1.7 7.2L12 17.8 5.7 21.5l1.7-7.2L2 9.6 9 9z"/></svg>
    <svg width="15" height="15" viewBox="0 0 24 24"><path fill="var(--star)" d="M12 2l3 7 7 .6-5.4 4.7 1.7 7.2L12 17.8 5.7 21.5l1.7-7.2L2 9.6 9 9z"/></svg>
    <svg width="15" height="15" viewBox="0 0 24 24"><path fill="var(--star)" d="M12 2l3 7 7 .6-5.4 4.7 1.7 7.2L12 17.8 5.7 21.5l1.7-7.2L2 9.6 9 9z"/></svg>
    <svg width="15" height="15" viewBox="0 0 24 24"><path fill="var(--star)" d="M12 2l3 7 7 .6-5.4 4.7 1.7 7.2L12 17.8 5.7 21.5l1.7-7.2L2 9.6 9 9z"/></svg>
    <svg width="15" height="15" viewBox="0 0 24 24"><path fill="var(--star)" d="M12 2l3 7 7 .6-5.4 4.7 1.7 7.2L12 17.8 5.7 21.5l1.7-7.2L2 9.6 9 9z"/></svg>
  </span>
</div>
<h1 class="abs display hero-title">Building with<br>precision,<br>safety, and<br>experience.</h1>
<p class="abs hero-text">From Site Preparation To Final Grading, We Deliver Dependable Excavation Solutions For Residential, Commercial, And Industrial Projects.</p>
<div class="btn btn-lime" style="left:50px;top:595px;width:184px;height:46px">Get a free quote</div>
<div class="btn btn-ghost" style="left:258px;top:595px;width:146px;height:46px">See projects</div>

<!-- About -->
<div class="photo" role="img" aria-label="Close view of a yellow excavator arm over a rocky site" style="left:0;top:695px;width:503px;height:730px;clip-path:polygon(0 0,100% 26%,100% 100%,0 100%);background:linear-gradient(170deg,#7d8279 0%,var(--photo-yellow) 40%,#4f514a 100%)"></div>
<div class="stat" style="left:608px;top:708px"><div class="stat-label">Projects Completed</div><div class="stat-value">800+</div></div>
<div class="stat" style="left:888px;top:708px"><div class="stat-label">Years Experience</div><div class="stat-value">20+</div></div>
<div class="stat" style="left:608px;top:835px"><div class="stat-label">Machinery Units</div><div class="stat-value">30+</div></div>
<div class="stat" style="left:888px;top:835px"><div class="stat-label">Safety Rating</div><div class="stat-value">100%</div></div>
<svg class="abs" style="left:1003px;top:1105px" width="115" height="120" viewBox="0 0 115 120">
  <circle cx="56" cy="64" r="54" fill="var(--badge-blue)"/>
  <path d="M68 8l8 8 11-2 3 11 10 5-4 11 5 10-9 7 1 11-11 2-5 10-10-5-10 5-5-10-11-2 1-11-9-7 5-10-4-11 10-5 3-11 11 2z" fill="none" stroke="#fff" stroke-width="2"/>
  <path d="M50 56l12 12 22-24" fill="none" stroke="#fff" stroke-width="5" stroke-linecap="round" stroke-linejoin="round"/>
</svg>
<h2 class="abs display about-title">Your Trusted<br>Earthworks<br>Partner</h2>
<p class="abs about-text">We Are A Professional Excavation &amp; Earthworks Company With Years Of Hands-On Experience In Delivering High-Quality Groundworks. Our Skilled Operators, Modern Machinery, And Commitment To Safety Ensure Every Project Is Completed On Time And To The Highest Standard.</p>
<div class="btn btn-lime" style="left:608px;top:1388px;width:137px;height:46px">Learn more</div>

<!-- Services -->
<svg class="abs" style="left:0;top:1440px" width="1200" height="672" viewBox="0 0 1200 672">
  <polygon points="0,45 1080,58 1200,12 1200,672 0,672" fill="var(--charcoal)"/>
</svg>
<h2 class="abs display section-title" style="left:83px;top:1545px">Our Services</h2>
<p class="abs" style="left:83px;top:1628px;font-size:13px">We Use Well-Maintained Machinery And Proven Techniques To Deliver Efficient, Cost-Effective Results.</p>
<a class="abs" style="left:971px;top:1612px;font-size:15px;font-weight:700;color:var(--lime)">MORE SERVICES</a>

<div class="service-card" style="left:83px">
  <h3>Excavation &amp;<br>Earthmoving</h3>
  <p>We Provide Precise And Efficient Excavation Services Using Modern Machinery. From Small Residential Digs To Large-Scale Earthmoving Projects, We Ensure Accuracy, Safety, And Minimal Site Disruption.</p>
  <div class="see-more">See more <svg width="16" height="14" viewBox="0 0 16 14" fill="none" stroke="var(--lime)" stroke-width="2"><path d="M1 7h13M9 2l5 5-5 5"/></svg></div>
</div>
<div class="service-card" style="left:433px">
  <h3>Site Preparation &amp;<br>Clearing</h3>
  <p>Our Site Preparation Services Ensure Your Land Is Ready For Construction. This Includes Clearing Vegetation, Removing Debris, And Leveling The Ground To Create A Stable And Compliant Worksite.</p>
  <div class="see-more">See more <svg width="16" height="14" viewBox="0 0 16 14" fill="none" stroke="var(--lime)" stroke-width="2"><path d="M1 7h13M9 2l5 5-5 5"/></svg></div>
</div>
<div class="service-card" style="left:783px">
  <h3>Trenching &amp;<br>Drainage</h3>
  <p>We Specialize In Trenching For Utilities, Plumbing, And Drainage Systems. Our Team Ensures Correct Depth, Alignment, And Proper Water Flow To Prevent Future Issues.</p>
  <div class="see-more">See more <svg width="16" height="14" viewBox="0 0 16 14" fill="none" stroke="var(--lime)" stroke-width="2"><path d="M1 7h13M9 2l5 5-5 5"/></svg></div>
</div>

<!-- Why choose us -->
<h2 class="abs display section-title" style="left:0;width:1200px;text-align:center;top:2230px">Why Choose Us</h2>
<div class="why-card" style="left:83px"><div class="why-icon"><svg width="26" height="26" viewBox="0 0 24 24" fill="none" stroke="#1a1a0a" stroke-width="2"><rect x="3" y="5" width="18" height="14" rx="1"/><circle cx="9" cy="11" r="2"/><path d="M14 10h4M14 14h4M6 16h6"/></svg></div><p>Experienced &amp; Licensed Operators</p></div>
<div class="why-card" style="left:258px"><div class="why-icon"><svg width="28" height="26" viewBox="0 0 28 24" fill="none" stroke="#1a1a0a" stroke-width="2"><rect x="2" y="10" width="12" height="7"/><path d="M8 10V5h5l3 5M14 13l6-8 5 6"/><circle cx="5" cy="20" r="2"/><circle cx="11" cy="20" r="2"/></svg></div><p>Modern Excavators &amp; Equipment</p></div>
<div class="why-card" style="left:433px"><div class="why-icon"><svg width="26" height="26" viewBox="0 0 24 24" fill="none" stroke="#1a1a0a" stroke-width="2"><path d="M12 2l8 3v6c0 5-3.5 9-8 11-4.5-2-8-6-8-11V5z"/><path d="M8 12l3 3 5-6"/></svg></div><p>Safety-First Approach</p></div>
<div class="why-card" style="left:608px"><div class="why-icon"><svg width="26" height="26" viewBox="0 0 24 24" fill="none" stroke="#1a1a0a" stroke-width="2"><path d="M3 21V8l9-5 9 5v13"/><path d="M7 21v-9h10v9M7 15h10M7 18h10"/></svg></div><p>On-Time Project Delivery</p></div>
<div class="why-card" style="left:783px"><div class="why-icon"><svg width="26" height="26" viewBox="0 0 24 24" fill="none" stroke="#1a1a0a" stroke-width="2"><path d="M12 2v20M17 6H9.5a3.5 3.5 0 0 0 0 7h5a3.5 3.5 0 0 1 0 7H6"/></svg></div><p>Competitive Pricing</p></div>
<div class="why-card" style="left:958px"><div class="why-icon"><svg width="26" height="26" viewBox="0 0 24 24" fill="#1a1a0a"><path d="M4 22V6h6V2h10v20zM6 9h2v2H6zm0 4h2v2H6zm0 4h2v2H6zm6-12h2v2h-2zm4 0h2v2h-2zm-4 4h2v2h-2zm4 0h2v2h-2zm-4 4h2v2h-2zm4 0h2v2h-2zm-4 4h2v2h-2zm4 0h2v2h-2z" fill-rule="evenodd"/></svg></div><p>Residential &amp; Commercial Expertise</p></div>

<!-- Testimonial -->
<h2 class="abs display" style="left:0;width:1200px;text-align:center;top:2588px;font-size:42px">Client Success Story</h2>
<div class="arrow-circle" style="left:205px;top:2783px"><svg width="14" height="14" viewBox="0 0 16 14" fill="none" stroke="#fff" stroke-width="2"><path d="M15 7H2M7 2L2 7l5 5"/></svg></div>
<div class="arrow-circle" style="left:964px;top:2783px"><svg width="14" height="14" viewBox="0 0 16 14" fill="none" stroke="#fff" stroke-width="2"><path d="M1 7h13M9 2l5 5-5 5"/></svg></div>
<div class="abs quote-card">
  <p style="font-size:15.5px;line-height:1.45;width:565px">“Lorem Ipsum is simply dummy text of the printing and typesetting industry. Lorem Ipsum has been the industry's standard dummy text ever since the 1500s”</p>
  <div class="stars" style="position:absolute;left:58px;top:158px">
    <svg width="17" height="17" viewBox="0 0 24 24"><path fill="var(--star)" d="M12 2l3 7 7 .6-5.4 4.7 1.7 7.2L12 17.8 5.7 21.5l1.7-7.2L2 9.6 9 9z"/></svg>
    <svg width="17" height="17" viewBox="0 0 24 24"><path fill="var(--star)" d="M12 2l3 7 7 .6-5.4 4.7 1.7 7.2L12 17.8 5.7 21.5l1.7-7.2L2 9.6 9 9z"/></svg>
    <svg width="17" height="17" viewBox="0 0 24 24"><path fill="var(--star)" d="M12 2l3 7 7 .6-5.4 4.7 1.7 7.2L12 17.8 5.7 21.5l1.7-7.2L2 9.6 9 9z"/></svg>
    <svg width="17" height="17" viewBox="0 0 24 24"><path fill="var(--star)" d="M12 2l3 7 7 .6-5.4 4.7 1.7 7.2L12 17.8 5.7 21.5l1.7-7.2L2 9.6 9 9z"/></svg>
    <svg width="17" height="17" viewBox="0 0 24 24"><path fill="var(--star)" d="M12 2l3 7 7 .6-5.4 4.7 1.7 7.2L12 17.8 5.7 21.5l1.7-7.2L2 9.6 9 9z"/></svg>
  </div>
  <div style="position:absolute;left:518px;top:140px">
    <div style="font-size:15px;font-weight:600">- Dana Whitlow</div>
    <div style="font-size:11px;margin-top:4px">Project owner</div>
  </div>
</div>
<div class="dot" style="left:578px"></div><div class="dot" style="left:589px"></div><div class="dot" style="left:600px"></div><div class="dot" style="left:611px"></div>

<!-- Call to action -->
<div class="abs cta"></div>
<div class="photo" role="img" aria-label="Yellow excavator arm resting on a gravel slope" style="left:702px;top:2905px;width:363px;height:515px;clip-path:polygon(0 18%,100% 0,100% 100%,0 100%);background:linear-gradient(165deg,#8a8f86 0%,#5e615a 35%,var(--photo-yellow) 65%,#4a4c46 100%)"></div>
<h2 class="abs display" style="left:117px;top:3108px;font-size:42px;line-height:48px;white-space:nowrap">Ready to Start Your<br>Project?</h2>
<p class="abs" style="left:117px;top:3228px;width:410px;font-size:13px;line-height:1.55">Get In Touch Today For Reliable Excavation And Earthworks Services You Can Trust.</p>
<div class="btn btn-lime" style="left:119px;top:3293px;width:184px;height:47px">Get a free quote</div>
<div class="btn btn-ghost" style="left:327px;top:3293px;width:147px;height:47px">See projects</div>

<!-- Footer -->
<footer class="abs footer"></footer>
<div class="abs brand" style="left:50px;top:3565px">
  <div class="brand-mark"></div>
  <div class="brand-name">Gullwind Stonecut<br>Earthworks</div>
</div>
<p class="abs" style="left:50px;top:3638px;width:275px;font-size:11px;line-height:1.6">Lorem Ipsum is simply dummy text of the printing and typesetting industry. Lorem Ipsum has been the industry's standard dummy text ever since the 1500s</p>
<div class="social" style="left:50px"></div>
<div class="social" style="left:94px"></div>
<div class="social" style="left:137px"></div>
<div class="social" style="left:181px"></div>

<h4 class="footer-heading" style="left:772px;top:3485px">Subscribe for Newsletter</h4>
<h4 class="footer-heading" style="left:422px;top:3588px">Services</h4>
<h4 class="footer-heading" style="left:592px;top:3588px">Company</h4>
<h4 class="footer-heading" style="left:886px;top:3588px">Contact Us</h4>
<div class="abs" style="left:772px;top:3521px;width:246px;height:45px;background:#fff;border-radius:4px 0 0 4px;color:#222;font-size:13px;padding:14px 18px">Enter Your Email</div>
<div class="btn btn-lime" style="left:1018px;top:3521px;width:132px;height:45px;border-radius:0 4px 4px 0;text-transform:none;font-size:13px">Subscribe</div>

<div class="footer-links">
  <a style="left:422px;top:3643px">Residential</a>
  <a style="left:422px;top:3688px">Commercial</a>
  <a style="left:422px;top:3733px">Machinery</a>
  <a style="left:422px;top:3778px">Safety</a>
  <a style="left:592px;top:3643px">About Us</a>
  <a style="left:592px;top:3688px">Why us</a>
  <a style="left:592px;top:3733px">News &amp; press</a>
  <a style="left:592px;top:3778px">Contact</a>
</div>
<div class="contact-row" style="top:3635px"><div class="contact-dot"><svg width="16" height="16" viewBox="0 0 24 24" fill="#1a1a0a"><path d="M5 3h4l2 5-3 2a12 12 0 0 0 6 6l2-3 5 2v4a2 2 0 0 1-2 2A17 17 0 0 1 3 5a2 2 0 0 1 2-2z"/></svg></div>+1 555-014-8720</div>
<div class="contact-row" style="top:3692px"><div class="contact-dot"><svg width="16" height="16" viewBox="0 0 24 24" fill="none" stroke="#1a1a0a" stroke-width="2.2"><rect x="3" y="5" width="18" height="14" rx="2"/><path d="M3 7l9 6 9-6"/></svg></div>hello@gullwindstonecut.example</div>
<div class="contact-row" style="top:3749px"><div class="contact-dot"><svg width="16" height="16" viewBox="0 0 24 24" fill="#1a1a0a"><path d="M12 2a7 7 0 0 0-7 7c0 5 7 13 7 13s7-8 7-13a7 7 0 0 0-7-7zm0 9.5a2.5 2.5 0 1 1 0-5 2.5 2.5 0 0 1 0 5z"/></svg></div>88 Quarry Road NY 41290</div>
<p class="abs" style="left:50px;top:3826px;font-size:12px">© Company- All Rights Reserved</p>

</body>
</html>
```